Card and board game developer website, small e-commerce site

We are designing a website for Spinning Otter Gadget Works. I need a homepage and a typical inside page designed.
The website navigation will be:
Home (where we'll introduce the games and the website)
Our Games (drops open into the two games)
Griffins of Morvandale
Quintessa
Order Now
About Us
Contact
The header of the website will include the logo, the navigation and a link to a facebook page. The header will also include a cart icon and a link to My Account.
Then on the homepage I suggest we include a row for each game:
Griffins of Morvandale
This row will include a photo (or maybe a series of photos that animate into each other) and quick info about the game plus two buttons: Info and Photos (which will go to the detail page with the photo gallery), and Order Now (which will take you to the product for ordering).
Quintessa
Your footer will contain a copyright note, plus links to:
Terms and conditions
Shipping and returns
FAQ
Contact
Account login
NOTE: the logo is the orange mokey. I've uploaded a brief with more information. The current website that we are redesigning is here https://www.spinningottergadget.example/
Please send me any questions that you have.
People interested in fun card and board games at home.
2 page

```html
<!DOCTYPE html>
<html lang="en">
<head>
<meta charset="utf-8">
<title>Spinning Otter Gadget Works — Home</title>
<link href="https://fonts.googleapis.com/css2?family=Exo+2:wght@400;500;600;700;800&display=swap" rel="stylesheet">
<style>
:root{
  --orange:#f28a2b;
  --bg:#10171b;
  --panel:#0c1316;
  --frame:#1e282d;
  --text:#d4d7d9;
  --white:#ffffff;
  --muted:#9aa1a5;
}
*{box-sizing:border-box;margin:0;padding:0}
html,body{width:777px;height:1200px;overflow:hidden}
body{position:relative;background:var(--bg);font-family:"Exo 2",sans-serif;color:var(--text)}
.hero{position:absolute;left:0;top:0;width:777px;height:362px;
  background:radial-gradient(ellipse at 72% 35%,#3a3325 0%,#221f19 35%,#15181a 70%,#101518 100%)}
.hero-art{position:absolute;inset:0}
.slash{position:absolute;left:0;width:777px;height:40px}
.site-header{position:absolute;left:0;top:0;width:777px;height:52px}
.brand{position:absolute;left:97px;top:17px;font-weight:800;font-size:17px;color:var(--orange);letter-spacing:.5px}
.main-nav{position:absolute;left:335px;top:20px;display:flex;gap:18px;font-size:8.5px;font-weight:600;color:var(--white)}
.main-nav a{color:inherit;text-decoration:none}
.main-nav .current{color:var(--orange)}
.social-dot{position:absolute;left:559px;top:21px;width:10px;height:10px;border-radius:50%;background:var(--white)}
.tool{position:absolute;top:16px;height:21px}
.tool span{position:absolute;top:5px;font-size:7.5px;font-weight:600;color:var(--white)}
.hero-badge{position:absolute;left:300px;top:115px;width:180px;text-align:center}
.hero-badge .dot{width:54px;height:54px;border-radius:50%;background:var(--orange);margin:0 auto 10px}
.hero-badge p{font-weight:700;font-size:15px;color:var(--white);line-height:1.2}
.section-title{position:absolute;left:0;top:388px;width:777px;text-align:center;font-size:20px;font-weight:700;color:var(--white)}
.title-rule{position:absolute;left:375px;top:413px;width:27px;height:2px;background:var(--orange);border-radius:1px}
.game-card{position:absolute;left:130px;width:517px;height:231px}
.game-card .frame{position:absolute;inset:0}
.game-photo{position:absolute;width:218px;height:192px}
.game-info{position:absolute;width:245px}
.game-title{font-size:12.5px;font-weight:700;color:var(--orange);margin-bottom:9px}
.game-info p{font-size:7px;line-height:9.7px;margin-bottom:9.7px;color:var(--text)}
.stats{display:flex;gap:18px;margin:2px 0 9px}
.stat{display:flex;align-items:center;gap:5px;font-size:7px;line-height:8px;color:var(--text)}
.stat b{display:block;color:var(--orange);font-weight:500}
.btn-row{position:absolute;display:flex;gap:9px}
.btn{position:relative;height:21px;font-size:7.5px;color:var(--text)}
.btn svg{position:absolute;inset:0}
.btn span{position:relative;display:block;text-align:center;line-height:21px}
.btn.primary{color:var(--orange)}
.site-footer{position:absolute;left:0;top:938px;width:777px;height:262px;
  background:radial-gradient(ellipse at 50% 60%,#1f2a23 0%,#151c1b 50%,#0f1517 100%)}
.footer-badge{position:absolute;left:330px;top:70px;width:116px;height:116px;border-radius:50%;background:var(--white);border:4px solid #3a2a1c;display:flex;align-items:center;justify-content:center;text-align:center;padding:14px;font-weight:700;font-size:11px;line-height:1.25;color:var(--orange)}
.footer-links{position:absolute;left:0;top:201px;width:777px;display:flex;justify-content:center;gap:16px;font-size:7.5px;color:var(--text)}
.footer-links a{color:inherit;text-decoration:none}
.footer-links .active{color:var(--orange);text-decoration:underline}
.copyright{position:absolute;left:0;top:215px;width:777px;text-align:center;font-size:7.5px;color:var(--text)}
.copyright span{color:var(--orange)}
</style>
</head>
<body>

<section class="hero">
  <div class="hero-art" role="img" aria-label="Dark photographic scene of a dragon in a shadowy forest"></div>
  <svg class="slash" style="top:318px" viewBox="0 0 777 40" width="777" height="40"><polygon points="200,28 577,0 505,25 230,28" fill="#f28a2b"/></svg>
</section>

<header class="site-header">
  <div class="brand">SOGW</div>
  <nav class="main-nav">
    <a class="current" href="#">Home</a>
    <a href="#">Our Games</a>
    <a href="#">About Us</a>
    <a href="#">Contact Us</a>
  </nav>
  <div class="social-dot" aria-label="Social page"></div>
  <div class="tool" style="left:578px;width:30px">
    <svg width="30" height="21" viewBox="0 0 30 21"><polygon points="1,10.5 7,1 23,1 29,10.5 23,20 7,20" fill="#0f1417" stroke="#f28a2b" stroke-width="1"/><circle cx="15" cy="8.5" r="2.3" fill="none" stroke="#f28a2b" stroke-width="1"/><path d="M11 14.5 Q15 10.5 19 14.5" fill="none" stroke="#f28a2b" stroke-width="1"/></svg>
  </div>
  <div class="tool" style="left:614px;width:65px">
    <svg width="65" height="21" viewBox="0 0 65 21"><polygon points="1,10.5 7,1 58,1 64,10.5 58,20 7,20" fill="#0f1417" stroke="#f28a2b" stroke-width="1"/><rect x="16" y="7" width="7" height="7" fill="none" stroke="#f28a2b" stroke-width="1"/><path d="M17.5 7 V5.5 Q19.5 3.5 21.5 5.5 V7" fill="none" stroke="#f28a2b" stroke-width="1"/></svg>
    <span style="left:29px">$ 0.00</span>
  </div>
</header>

<div class="hero-badge">
  <div class="dot"></div>
  <p>Spinning Otter Gadget Works</p>
</div>

<h2 class="section-title">Our Games</h2>
<div class="title-rule"></div>

<article class="game-card" style="top:422px">
  <svg class="frame" width="517" height="231" viewBox="0 0 517 231"><path d="M1.5 9 L9 1.5 L117 1.5 L127 10.5 L509 10.5 L515.5 17 L515.5 223 L509 229.5 L9 229.5 L1.5 223 Z" fill="#0c1316" stroke="#1e282d" stroke-width="3"/></svg>
  <div class="game-photo" style="left:13px;top:26px;background:linear-gradient(135deg,#dcdbe0,#c9c8cf);" role="img" aria-label="Photo of the Griffins of Morvandale game box"></div>
  <div class="game-info" style="left:256px;top:32px">
    <h3 class="game-title">Griffins of Morvandale</h3>
    <p>Welcome to The Griffins Of Morvandale, the first board game where every player is a GRIFFIN.</p>
    <p>Conquer territory and build your empire.  Plunder castles and collect a huge hoard of gold. Rescue relatively attractive royalty or maybe eat them.  Who knows?  All we know is that everyone's a winner when the pizza's delivered!**</p>
    <div class="stats">
      <div class="stat"><svg width="13" height="13" viewBox="0 0 13 13"><circle cx="6.5" cy="4" r="2.8" fill="none" stroke="#bfc4c7"/><path d="M1 12 Q6.5 5 12 12 Z" fill="none" stroke="#bfc4c7"/></svg><div><b>2 - 6</b>players *</div></div>
      <div class="stat"><svg width="13" height="13" viewBox="0 0 13 13"><circle cx="6.5" cy="6.5" r="5.5" fill="none" stroke="#bfc4c7"/><path d="M6.5 3.5 V6.5 L8.5 8" fill="none" stroke="#bfc4c7"/></svg><div><b>1.5 hours.</b>Playtime approximately</div></div>
    </div>
    <p>* Game comes with 4 griffin packs.  Additional griffin expansion packs coming soon.</p>
  </div>
  <div class="btn-row" style="left:258px;top:188px">
    <div class="btn" style="width:78px"><svg width="78" height="21" viewBox="0 0 78 21"><polygon points="1,10.5 6,1 72,1 77,10.5 72,20 6,20" fill="#12191c" stroke="#8a9094" stroke-width="1"/></svg><span>Info &amp; Photos</span></div>
    <div class="btn primary" style="width:68px"><svg width="68" height="21" viewBox="0 0 68 21"><polygon points="1,10.5 6,1 62,1 67,10.5 62,20 6,20" fill="#12191c" stroke="#f28a2b" stroke-width="1"/><polygon points="3,10.5 6,7.5 6,13.5" fill="#f28a2b"/><polygon points="65,10.5 62,7.5 62,13.5" fill="#f28a2b"/></svg><span>Order Now</span></div>
  </div>
</article>

<article class="game-card" style="top:673px">
  <svg class="frame" width="517" height="231" viewBox="0 0 517 231"><path d="M1.5 17 L8 10.5 L390 10.5 L400 1.5 L508 1.5 L515.5 9 L515.5 223 L508 229.5 L9 229.5 L1.5 223 Z" fill="#0c1316" stroke="#1e282d" stroke-width="3"/></svg>
  <div class="game-info" style="left:15px;top:29px">
    <h3 class="game-title">Quintessa</h3>
    <p>Welcome to Quintessa, a fast paced card game of strategy and chance.  Play your element cards (Earth, Air, Fire,Water) and wild cards (Guardian, Balance, Evolution, Genesis) wisely and be the first player to discard all of their cards and declare yourself the master of the elements.</p>
    <div class="stats">
      <div class="stat"><svg width="13" height="13" viewBox="0 0 13 13"><circle cx="6.5" cy="4" r="2.8" fill="none" stroke="#bfc4c7"/><path d="M1 12 Q6.5 5 12 12 Z" fill="none" stroke="#bfc4c7"/></svg><div><b>X - X</b>players *</div></div>
      <div class="stat"><svg width="13" height="13" viewBox="0 0 13 13"><circle cx="6.5" cy="6.5" r="5.5" fill="none" stroke="#bfc4c7"/><path d="M6.5 3.5 V6.5 L8.5 8" fill="none" stroke="#bfc4c7"/></svg><div><b>X.X hours.</b>Playtime approximately</div></div>
    </div>
    <p>* Game comes with 4 griffin packs.  Additional griffin expansion packs coming soon.</p>
  </div>
  <div class="btn-row" style="left:17px;top:188px">
    <div class="btn" style="width:78px"><svg width="78" height="21" viewBox="0 0 78 21"><polygon points="1,10.5 6,1 72,1 77,10.5 72,20 6,20" fill="#12191c" stroke="#8a9094" stroke-width="1"/></svg><span>Info &amp; Photos</span></div>
    <div class="btn" style="width:68px"><svg width="68" height="21" viewBox="0 0 68 21"><polygon points="1,10.5 6,1 62,1 67,10.5 62,20 6,20" fill="#12191c" stroke="#8a9094" stroke-width="1"/></svg><span>Order Now</span></div>
  </div>
  <div class="game-photo" style="left:285px;top:25px;background:linear-gradient(135deg,#ececf0,#dcdce2);" role="img" aria-label="Photo of the Quintessa card deck"></div>
</article>

<footer class="site-footer">
  <div role="img" aria-label="Dim photo of a game board with pieces and dice" style="position:absolute;inset:0"></div>
  <svg class="slash" style="top:14px" viewBox="0 0 777 40" width="777" height="40"><polygon points="200,28 272,3 585,0 450,10" fill="#f28a2b"/></svg>
  <div class="footer-badge">Spinning Otter Gadget Works</div>
  <nav class="footer-links">
    <a href="#">Terms and conditions</a>
    <a href="#">Shipping and returns</a>
    <a href="#">FAQ</a>
    <a href="#">Contact</a>
    <a class="active" href="#">Account login</a>
  </nav>
  <p class="copyright">© 2024 <span>Spinning Otter Gadget.</span> All Rights Reserved</p>
</footer>

</body>
</html>
```